professional business card

A Clean looking business card for a money transfer company. Our company is call Velorix= Transfer + Send = Transcend (next level)
to show professionalism as well as some effects to show digital tech.

1 side to have position, name and address
2 side to have company name and show that we provide money exchange and cross-border money transfer

Target Market(s)

Remittance companies and high net worth individuals

Industry/Entity Type

Finance

Contact Information for Business Card

Name, address, email, title, services- money exchange and cross-border remittance

Requirements
Nice to have
• Digital age feel

```html
<!DOCTYPE html>
<html lang="en">
<head>
<meta charset="utf-8">
<title>Velorix Business Card</title>
<link href="https://fonts.googleapis.com/css2?family=Montserrat:wght@500&family=Open+Sans:wght@400;600;700&display=swap" rel="stylesheet">
<style>
  :root {
    --backdrop: #dcdde0;
    --card-white: #ffffff;
    --navy: #132838;
    --teal: #6cc5d1;
    --teal-soft: rgba(108, 197, 209, 0.28);
    --ink: #1d2b36;
  }
  * { margin: 0; padding: 0; box-sizing: border-box; }
  html, body {
    width: 1200px;
    height: 803px;
    overflow: hidden;
    background: var(--backdrop);
  }
  .canvas {
    position: relative;
    width: 1200px;
    height: 803px;
  }
  .card {
    position: absolute;
    top: 275px;
    width: 450px;
    height: 258px;
    overflow: hidden;
  }
  .card--front {
    left: 95px;
    background: var(--card-white);
    font-family: "Open Sans", sans-serif;
    color: var(--ink);
  }
  .card--back {
    left: 655px;
    background: var(--navy);
  }

  /* Front */
  .front-wordmark {
    position: absolute;
    left: 96px;
    top: 48px;
    font-family: "Open Sans", sans-serif;
    font-weight: 700;
    font-size: 30px;
    color: var(--teal);
  }
  .holder {
    position: absolute;
    right: 240px;
    top: 150px;
    text-align: right;
  }
  .holder-name {
    font-weight: 700;
    font-size: 15px;
    color: var(--teal);
    line-height: 1.2;
  }
  .holder-title {
    font-size: 12px;
    color: var(--ink);
    line-height: 1.3;
  }
  .divider {
    position: absolute;
    left: 224px;
    top: 108px;
    width: 1px;
    height: 100px;
    background: var(--teal);
  }
  .contact {
    position: absolute;
    left: 238px;
    top: 108px;
    font-size: 11.5px;
    line-height: 1.35;
    list-style: none;
  }
  .contact-address { margin-bottom: 4px; }
  .contact-item {
    display: flex;
    align-items: center;
    gap: 5px;
    margin-top: 2px;
  }
  .contact-icon { width: 12px; height: 12px; flex: none; }

  /* Back */
  .circuit {
    position: absolute;
    inset: 0;
    width: 100%;
    height: 100%;
  }
  .back-content {
    position: absolute;
    inset: 0;
    display: flex;
    flex-direction: column;
    align-items: center;
    justify-content: center;
    gap: 14px;
  }
  .back-brand {
    display: flex;
    align-items: center;
    gap: 12px;
  }
  .back-dot {
    width: 22px;
    height: 22px;
    border-radius: 50%;
    background: var(--teal);
  }
  .back-wordmark {
    font-family: "Montserrat", sans-serif;
    font-weight: 500;
    font-size: 40px;
    letter-spacing: 1px;
    color: var(--card-white);
    line-height: 1;
  }
  .services {
    display: flex;
    align-items: center;
    gap: 10px;
    font-family: "Open Sans", sans-serif;
    font-weight: 600;
    font-size: 10px;
    letter-spacing: 1.6px;
    text-transform: uppercase;
    color: var(--teal);
  }
  .services-sep {
    width: 4px;
    height: 4px;
    border-radius: 50%;
    background: var(--teal);
  }
</style>
</head>
<body>
<main class="canvas">
  <section class="card card--front" aria-label="Business card front">
    <div class="front-wordmark">Velorix</div>
    <div class="holder">
      <div class="holder-name">Daniel Reyes</div>
      <div class="holder-title">Manager</div>
    </div>
    <div class="divider"></div>
    <ul class="contact">
      <li class="contact-address">2840, Harbor Lane,<br>Oakridge, CA 90210</li>
      <li class="contact-item">
        <svg class="contact-icon" viewBox="0 0 12 12" aria-hidden="true">
          <circle cx="6" cy="6" r="6" fill="var(--navy)"/>
          <path d="M3.6 3.2l1.2-.4.7 1.5-.7.6c.3.8.9 1.4 1.7 1.7l.6-.7 1.5.7-.4 1.2C6 7.9 4.1 6 3.6 3.2z" fill="#fff"/>
        </svg>
        555-318-2047
      </li>
      <li class="contact-item">
        <svg class="contact-icon" viewBox="0 0 12 12" aria-hidden="true">
          <circle cx="6" cy="6" r="6" fill="var(--navy)"/>
          <rect x="3" y="4" width="6" height="4" fill="none" stroke="#fff" stroke-width=".8"/>
          <path d="M3 4l3 2.2L9 4" fill="none" stroke="#fff" stroke-width=".8"/>
        </svg>
        info@velorix.com
      </li>
      <li class="contact-item">
        <svg class="contact-icon" viewBox="0 0 12 12" aria-hidden="true">
          <circle cx="6" cy="6" r="6" fill="var(--navy)"/>
          <circle cx="6" cy="6" r="3" fill="none" stroke="#fff" stroke-width=".7"/>
          <path d="M3 6h6M6 3c-1.3 1.6-1.3 4.4 0 6M6 3c1.3 1.6 1.3 4.4 0 6" fill="none" stroke="#fff" stroke-width=".6"/>
        </svg>
        www.velorix.com
      </li>
    </ul>
  </section>

  <section class="card card--back" aria-label="Business card back">
    <svg class="circuit" viewBox="0 0 450 258" aria-hidden="true">
      <g fill="none" stroke="var(--teal-soft)" stroke-width="1">
        <path d="M0 30h60l20 20h50"/>
        <path d="M0 48h40l14 14h30"/>
        <path d="M450 210h-70l-20-20h-46"/>
        <path d="M450 228h-44l-14-14h-34"/>
        <path d="M330 258v-20l12-12"/>
        <path d="M110 0v18l-12 12"/>
      </g>
      <g fill="var(--teal-soft)">
        <circle cx="130" cy="50" r="3"/>
        <circle cx="84" cy="62" r="2.5"/>
        <circle cx="314" cy="190" r="3"/>
        <circle cx="358" cy="214" r="2.5"/>
        <circle cx="342" cy="226" r="2.5"/>
        <circle cx="98" cy="30" r="2.5"/>
      </g>
    </svg>
    <div class="back-content">
      <div class="back-brand">
        <span class="back-dot"></span>
        <span class="back-wordmark">VELORIX</span>
      </div>
      <div class="services">
        <span>Money Exchange</span>
        <span class="services-sep"></span>
        <span>Cross-Border Remittance</span>
      </div>
    </div>
  </section>
</main>
</body>
</html>
```